IT Consulting & Staff Augmentation Page

Hi,
I eliminated your design for the initial project, but I would like that very same design for our Staff Augmentation page
http://staging.brightvaleworks.com/staff-augmentation/

The photo of the people sitting around is not nearly as powerful as your drawing. I think it's cool!

And for the IT consulting....http://staging.brightvaleworks.com/it-consulting-2/
I'm looking for a little graphic, accent or whatever for each of those 4 buckets.

Other designers are welcomed to submit!!

Industry/Entity Type

Consulting

```html
<!DOCTYPE html>
<html lang="en">
<head>
<meta charset="utf-8">
<title>Brightvale Works – IT Consulting</title>
<link href="https://fonts.googleapis.com/css2?family=Source+Sans+3:ital,wght@0,400;0,600;0,700;0,800;1,700;1,800&family=Raleway:wght@600&display=swap" rel="stylesheet">
<style>
:root{
  --dark:#222a30;
  --nav:#2c2f33;
  --yellow:#e7d93b;
  --title-yellow:#efe04a;
  --card:#efefef;
  --ink:#1d1d1d;
  --body:#333;
  --white:#fff;
  --accent-red:#d42a1e;
}
*{box-sizing:border-box;margin:0;padding:0}
html,body{width:936px;height:1200px;overflow:hidden;background:var(--white)}
body{position:relative;font-family:"Source Sans 3",Arial,sans-serif;color:var(--body)}
.abs{position:absolute}

.topbar{left:0;top:0;width:936px;height:47px;background:var(--nav);border-bottom:1px solid #9a9a4a}
.brand{left:208px;top:9px;display:flex;align-items:center;gap:8px;color:var(--white);font-weight:700;font-size:19px}
.brand-mark{width:22px;height:22px;background:var(--yellow)}
.nav{right:101px;top:18px;display:flex;gap:16px;font-family:"Raleway",Arial,sans-serif;font-size:7.5px;color:var(--white);letter-spacing:.3px}
.nav svg{margin-top:-1px}

.hero{left:0;top:48px;width:936px;height:241px;background:radial-gradient(ellipse at 50% 55%,#77787a 0%,#4f5052 45%,#2c2d2f 100%)}

.title-band{left:0;top:289px;width:936px;height:61px;background:var(--dark);text-align:center}
.title-band h1{margin-top:6px;font-size:28px;font-weight:800;color:var(--title-yellow);letter-spacing:.2px;line-height:1.1}
.title-band p{font-size:16px;font-weight:800;font-style:italic;color:var(--white);line-height:1.1}

.intro-art{left:209px;top:380px;width:106px;height:95px;background:linear-gradient(135deg,#6a8fc9,#2f5da8 55%,#222);border-radius:6px}
.intro h2{left:318px;top:391px;font-size:21px;font-weight:800;color:var(--ink)}
.intro p{left:320px;top:420px;width:236px;font-size:8.6px;line-height:11.2px;color:#333}

.card{left:218px;width:332px;background:var(--card);border-radius:5px}
.card h3{position:absolute;font-size:12.3px;font-weight:700;color:var(--ink);line-height:14.5px}
.card p{position:absolute;font-size:8.4px;line-height:11.2px;color:#333}
.card .art{position:absolute;background:linear-gradient(160deg,#f3c89a,#9bc2e6 55%,#8a8a8a);border-radius:4px;opacity:.85}

.c1{top:505px;height:119px}
.c2{top:636px;height:119px}
.c3{top:768px;height:152px}
.c4{top:934px;height:152px}

.closing{left:223px;top:1100px;width:320px;font-size:12.3px;line-height:15px;font-weight:800;font-style:italic;color:var(--ink)}

.side-brand{left:608px;top:361px;font-size:17px;font-weight:700;color:var(--ink)}
.form-panel{left:571px;top:397px;width:156px;height:415px;background:var(--yellow)}
.form-notch{left:639px;top:397px;width:0;height:0;border-left:12px solid transparent;border-right:12px solid transparent;border-top:12px solid var(--white)}
.form-title{left:591px;top:406px;color:var(--ink);font-style:italic;font-weight:800;line-height:1}
.form-title small{display:block;font-size:11px}
.form-title span{display:block;font-size:20px;line-height:23px;margin-top:3px}
.field{left:581px;width:132px}
.field label{display:block;font-size:7.4px;font-weight:700;color:var(--ink);margin-bottom:3px}
.field .input{height:20px;background:var(--white);position:relative}
.field .caret{position:absolute;right:4px;top:7px;border-left:5px solid transparent;border-right:5px solid transparent;border-top:6px solid #555}
.submit{left:583px;top:762px;width:130px;height:36px;border-radius:6px;background:linear-gradient(#fffbe0,#f1e28a);box-shadow:0 2px 2px rgba(0,0,0,.35);text-align:center;line-height:36px;font-size:13px;font-weight:700;color:var(--ink)}
.submit-arrow{left:576px;top:755px}

.footer{left:0;top:1177px;width:936px;height:23px;background:var(--dark)}
</style>
</head>
<body>

<header class="abs topbar"></header>
<div class="abs brand"><span class="brand-mark"></span>Brightvale Works</div>
<nav class="abs nav">
  <span>SERVICES</span><span>PROJECTS</span><span>BLOG</span><span>CONTACT</span>
  <svg width="8" height="8" viewBox="0 0 10 10"><circle cx="4" cy="4" r="3" fill="none" stroke="#fff" stroke-width="1.6"/><line x1="6.3" y1="6.3" x2="9.3" y2="9.3" stroke="#fff" stroke-width="1.6"/></svg>
</nav>

<div class="abs hero" role="img" aria-label="Photo of a team of business professionals in suits standing behind a close-up handshake, with a faint world map behind them"></div>

<section class="abs title-band">
  <h1>STRONG TEAM OF IT PROFESSIONAL</h1>
  <p>WITH ROOTS IN ALL THINGS GEEKY</p>
</section>

<div class="abs intro-art" role="img" aria-label="Illustration of a businessman with a briefcase leaning on a globe"></div>
<div class="intro">
  <h2 class="abs">IT CONSULTING</h2>
  <p class="abs">Whether you need to bolster your IT department or provide technical experts where none exist, Brightvale’s Staff Augmentation (“SA”) service enables your company to do so without the daunting challenges associated with not only hiring but maintaining qualified technology professionals.</p>
</div>

<article class="abs card c1">
  <h3 style="left:15px;top:9px">It’s like having a big brother!<br>Just not as annoying.</h3>
  <p style="left:15px;top:45px;width:190px">We all love the idea of “One Stop” shopping. But, how do you do that in the IT industry without looking like the “Jack of all trades and master of none”. And so it dawned on us…<br>PRIMARY CARE TECHNOLOGIST!</p>
  <div class="art" style="left:224px;top:15px;width:82px;height:90px" role="img" aria-label="Cartoon of two office workers shaking hands"></div>
</article>

<article class="abs card c2">
  <div class="art" style="left:34px;top:6px;width:48px;height:106px" role="img" aria-label="Cartoon of a puzzled office worker with question marks above his head"></div>
  <h3 style="left:114px;top:9px">What does this mean?</h3>
  <p style="left:114px;top:29px;width:206px">Analogy: If you have a fever you go see your doctor, right? The doctor looks you over, and may refer you to a specialist if they think it’s necessary. They may recommend seeing a Hematologist. Your first thought is, “Gee I don’t know any Hematologists??” And so you ask your doctor if they can recommend a good one because you trust them. They’re doctors!</p>
</article>

<article class="abs card c3">
  <h3 style="left:16px;top:9px">Why should you go somewhere else?</h3>
  <p style="left:16px;top:30px;width:212px">We like most IT Professionals started out in this business as GEEKs and along the way we specialized. We became software, mobile and web design experts. But, Brightvale has not forgotten its roots in all things GEEKY, and stays current on the latest trends in computer hardware and networking. In fact we still do our own tech support “in-house”. If a client was to come to us looking for custom software and in our discussions we determine a server is needed…<br>well we could do that!</p>
  <div class="art" style="left:236px;top:28px;width:96px;height:100px" role="img" aria-label="Cartoon of an office worker presenting a rising line chart"></div>
</article>

<article class="abs card c4">
  <div class="art" style="left:26px;top:10px;width:52px;height:133px" role="img" aria-label="Cartoon of an office worker with a light bulb idea above his head"></div>
  <h3 style="left:110px;top:9px">We are in the Biz!</h3>
  <p style="left:110px;top:29px;width:210px">We are IT Professionals, and as we stated, IT Consulting is in our bloodlines. For our clients we have acquired, interviewed, referred, recommended and utilized qualified Network Administrators, PC Support Specialists, and Disaster Recovery specialists on projects not pertaining to the core of our business, which is software application and web design. This is because we have longstanding relationships within the industry and our clients trust our judgment. So should you!</p>
</article>

<p class="abs closing">And it’s on us if that resource does not work out…but, we’re not worried about that because we only deal with great people!</p>

<aside>
  <div class="abs side-brand">Brightvale</div>
  <div class="abs form-panel"></div>
  <div class="abs form-notch"></div>
  <div class="abs form-title"><small>THE</small><span>DIFFERENCE<br>BEGINS HERE</span></div>

  <div class="abs field" style="top:478px"><label>First Name *</label><div class="input"></div></div>
  <div class="abs field" style="top:516px"><label>Last Name *</label><div class="input"></div></div>
  <div class="abs field" style="top:554px"><label>Business Email *</label><div class="input"></div></div>
  <div class="abs field" style="top:592px"><label>Title *</label><div class="input"></div></div>
  <div class="abs field" style="top:630px"><label>Business Phone *</label><div class="input"></div></div>
  <div class="abs field" style="top:672px"><label>State or Province *</label><div class="input"></div></div>
  <div class="abs field" style="top:715px"><label>Country *</label><div class="input"><span class="caret"></span></div></div>

  <div class="abs submit">Request Contact</div>
  <svg class="abs submit-arrow" width="30" height="26" viewBox="0 0 30 26">
    <path d="M4 24 C2 12 10 5 20 6" fill="none" stroke="var(--accent-red)" stroke-width="4" stroke-linecap="round"/>
    <path d="M17 0 L28 7 L17 12 Z" fill="var(--accent-red)"/>
  </svg>
</aside>

<footer class="abs footer"></footer>

</body>
</html>
```